Oil and Gas Company: Letterhead Design

In short we need a professional company letterhead designed for our Oil and Gas company.

We would like to keep the design simple and professional. Letterhead to include the company logo and color scheme, front page and continuation pages.

For reference, see attached logo below with our company logo and color scheme.

Target Market(s)

Oil & Gas Market

Industry/Entity Type

Oil And Gas

Font styles to use
Sans Serif

Requirements
Must have
• Letterhead must contain a front page & continuation page.
• Must be simple and professional in design.
• Follow our logo and color scheme.
Nice to have
• I would like to have the logo embedded in the bottom right hand portion of the page to provide some depth into the letterhead.

```html
<!DOCTYPE html>
<html lang="en">
<head>
<meta charset="utf-8">
<title>Redline Basin Energy — Letterhead</title>
<link href="https://fonts.googleapis.com/css2?family=Kumbh+Sans:wght@300;400;500&display=swap" rel="stylesheet">
<style>
  :root{
    --bg:#8e979f;
    --paper:#ffffff;
    --red:#e31e26;
    --blue:#0f4fa8;
    --ink:#1b1b1b;
    --text:#7a7a7a;
    --muted:#9a9a9a;
    --band-grey:#e6e6e6;
    --map:#f1f1f1;
  }
  *{margin:0;padding:0;box-sizing:border-box}
  html,body{width:1200px;height:1200px;overflow:hidden}
  body{background:var(--bg);font-family:"Kumbh Sans",sans-serif;position:relative}
  .letterhead{
    position:absolute;left:183px;top:10px;width:834px;height:1180px;
    background:var(--paper);overflow:hidden;
  }
  .header-band{
    position:absolute;left:0;top:0;width:834px;height:67px;
    background:linear-gradient(90deg,var(--red) 0%,#ee6a6f 20%,#6f8fc4 30%,var(--blue) 50%,#6f8fc4 70%,#ee6a6f 80%,var(--red) 100%);
  }
  .brand-mark{
    position:absolute;left:389px;top:64px;width:56px;height:56px;border-radius:50%;
    background:var(--red);
  }
  .company-name{
    position:absolute;left:0;top:141px;width:834px;text-align:center;
    font-weight:500;font-size:16.5px;line-height:18px;letter-spacing:.6px;color:var(--ink);
    text-transform:uppercase;
  }
  .letter{
    position:absolute;left:175px;top:286px;width:587px;
    color:var(--text);font-weight:300;font-size:15.3px;line-height:20px;
  }
  .letter .date{margin-bottom:28px}
  .letter .recipient{line-height:17px;margin-bottom:45px}
  .letter .salutation{margin-bottom:20px}
  .letter .body p{text-align:justify;margin-bottom:14px}
  .letter .closing{margin-top:43px;margin-bottom:37px}
  .letter .signature{line-height:17px}
  .world-map{
    position:absolute;left:342px;top:890px;width:480px;height:230px;
    background:radial-gradient(ellipse at 55% 45%,var(--map) 0%,#f7f7f7 50%,rgba(255,255,255,0) 72%);
  }
  .contact-bar{
    position:absolute;left:247px;top:1130px;display:flex;gap:18px;align-items:center;
    font-weight:500;font-size:6.5px;letter-spacing:.8px;line-height:10px;color:var(--muted);
    text-transform:uppercase;
  }
  .contact-item{display:flex;align-items:center;gap:12px}
  .contact-item svg{width:20px;height:20px;display:block}
  .footer-band{
    position:absolute;left:0;bottom:0;width:834px;height:20px;
    background:linear-gradient(90deg,var(--red) 0%,var(--red) 56%,var(--band-grey) 56%,var(--band-grey) 100%);
  }
</style>
</head>
<body>
<main class="letterhead">
  <div class="header-band" role="img" aria-label="Diagonal red and blue stripe band forming a chevron"></div>
  <div class="brand-mark" aria-hidden="true"></div>
  <div class="company-name">Redline Basin<br>Energy</div>

  <article class="letter">
    <p class="date">August 28, 2011</p>
    <p class="recipient">First Last Name<br>Street Address<br>City, State 00000</p>
    <p class="salutation">Dear &lt;First Name&gt;:</p>
    <div class="body">
      <p>Lorem ipsum dolor sit amet, consectetur adipiscing elit. Aenean ut ipsum eget massa hendrerit vestibulum vel in velit. Donec pretium neque velit.</p>
      <p>Aliquam porta lectus nec mauris ornare venenatis. Vivamus non est turpis, et cursus sem. Mauris vehicula erat in diam auctor at bibendum nisl lacinia.</p>
      <p>Morbi imperdiet neque vehicula nunc convallis gravida. Vestibulum iaculis pretium placerat. Integer consequat, est sit amet facilisis eleifend, nibh nibh varius orci, eget dapibus arcu dui non purus. Pellentesque in magna mauris. Duis enim sapien, dictum vitae condimentum a, pulvinar vel lacus. Mauris et molestie nibh. Vestibulum vitae nulla at metus elementum porta sit amet interdum elit. Nulla sollicitudin neque eu nulla volutpat congue.</p>
      <p>Etiam pellentesque, velit id dapibus fermentum, turpis sapien ornare dui, ac tincidunt ligula odio congue purus. Nunc sed ante dui, in porta lectus. Cras nec sem lorem. In hac habitasse platea dictumst. Maecenas id diam quis dui porta tristique. Sed id egestas felis. Donec ullamcorper mattis posuere. Phasellus fermentum eleifend tortor vel dapibus. Vestibulum ante ipsum.</p>
    </div>
    <p class="closing">Sincerely,</p>
    <p class="signature">Daniel Marsh<br>RedlineBasin.com<br>P.O. Box 41120<br>Granby, CO 80446<br>P: (970) 555-0182</p>
  </article>

  <div class="world-map" role="img" aria-label="Faint dotted world map watermark"></div>

  <footer class="contact-bar">
    <div class="contact-item">
      <svg viewBox="0 0 20 20" aria-hidden="true"><circle cx="10" cy="10" r="10" fill="#9a9a9a"/><path d="M7 5.5l1.6 2.4-1 1.1c.6 1.3 1.5 2.2 2.8 2.8l1.1-1 2.4 1.6-.9 1.8c-3.7-.3-6.6-3.2-6.9-6.9z" fill="#fff"/></svg>
      <span>+12 123 456 7890<br>+12 123 456 7890</span>
    </div>
    <div class="contact-item">
      <svg viewBox="0 0 20 20" aria-hidden="true"><circle cx="10" cy="10" r="10" fill="#9a9a9a"/><g fill="none" stroke="#fff" stroke-width="1"><circle cx="10" cy="10" r="5.5"/><ellipse cx="10" cy="10" rx="2.4" ry="5.5"/><path d="M4.5 10h11M5.3 7.3h9.4M5.3 12.7h9.4"/></g></svg>
      <span>info@email.com<br>yourwebsite.com</span>
    </div>
    <div class="contact-item">
      <svg viewBox="0 0 20 20" aria-hidden="true"><circle cx="10" cy="10" r="10" fill="#9a9a9a"/><path d="M10 4.5a3.6 3.6 0 0 0-3.6 3.6c0 2.7 3.6 7 3.6 7s3.6-4.3 3.6-7A3.6 3.6 0 0 0 10 4.5z" fill="#fff"/><circle cx="10" cy="8.1" r="1.3" fill="#9a9a9a"/></svg>
      <span>Your street address<br>Main avenue, NY city, USA</span>
    </div>
  </footer>

  <div class="footer-band" role="img" aria-label="Red and light grey diagonal stripe band"></div>
</main>
</body>
</html>
```